Brightpath Home Partners, LLC

We are private duty home care agency. We provide in-home care for people of all ages. Our kind natured and patient caregivers provide assistance to those who have difficulty with caring for themselves. We already have a logo designed by ArtMarketly

```html
<!DOCTYPE html>
<html lang="en">
<head>
<meta charset="utf-8">
<title>Brightpath Home Partners, LLC</title>
<link href="https://fonts.googleapis.com/css2?family=Raleway:wght@400;500;600;700&display=swap" rel="stylesheet">
<style>
:root{
  --green:#2f8a0c;
  --green-dark:#247008;
  --orange:#f96f10;
  --ink:#1d1d1d;
  --text:#333;
  --gray-bg:#e9e9e9;
  --nav-bg:#f1f1f1;
  --footer:#3a3a3a;
}
*{margin:0;padding:0;box-sizing:border-box}
html,body{width:1200px;height:3768px;overflow:hidden}
body{font-family:'Raleway',sans-serif;color:var(--text);background:#fff;position:relative}
.abs{position:absolute}
.topbar{top:0;left:0;width:1200px;height:41px;background:var(--green);color:#fff;font-size:13px}
.topbar span{position:absolute;top:12px}
.topbar .sep{position:absolute;top:0;width:1px;height:41px;background:rgba(255,255,255,.35)}
.header{top:41px;left:0;width:1200px;height:111px;background:#fff}
.call{left:142px;top:30px;display:flex;align-items:center;gap:10px}
.call .ring{width:40px;height:40px;border:3px solid var(--orange);border-radius:50%;display:flex;align-items:center;justify-content:center}
.call b{color:var(--green);font-size:15px;display:block}
.call small{font-size:14px;color:var(--ink)}
.brand{left:0;width:1200px;top:32px;text-align:center;color:var(--green);font-size:34px;font-weight:700;letter-spacing:.5px}
.brand small{display:block;font-size:15px;font-weight:700;letter-spacing:3px;margin-top:2px}
.search{left:831px;top:30px;width:263px;height:52px;border:1px solid #ddd;border-radius:26px;padding:15px 20px;font-size:16px;color:#777}
.search i{position:absolute;right:6px;top:7px;width:38px;height:38px;border-radius:50%;background:var(--orange);display:flex;align-items:center;justify-content:center}
.nav{top:152px;left:0;width:1200px;height:65px;background:var(--nav-bg);border-top:1px solid #ddd;display:flex;justify-content:center;gap:46px;align-items:center;font-size:17px;color:var(--ink)}
.hero{top:217px;left:0;width:1200px;height:675px;background:linear-gradient(100deg,#8b6a52 0%,#c9b3a0 30%,#e8e2da 60%,#d6cfc6 100%)}
.hero-name{left:620px;top:440px;color:var(--green);font-size:62px;font-weight:700;line-height:1}
.hero-name small{display:block;font-size:26px;margin-top:10px;letter-spacing:3px}
.center{left:0;width:1200px;text-align:center}
h2{color:var(--green);font-weight:700;font-size:35px}
.kicker{font-size:22px;font-weight:600;color:var(--ink)}
.lead{font-size:17px;line-height:32px;color:var(--ink)}
.form{top:1099px;left:89px;width:1021px;height:99px;background:#fff;box-shadow:0 2px 8px rgba(0,0,0,.12);display:flex}
.field{flex:0 0 420px;padding:24px 10px;border-right:1px solid #ddd;position:relative}
.field:nth-child(2){flex-basis:422px;padding-left:29px}
.field small{font-size:12px;color:var(--ink);font-weight:600;display:block}
.field span{font-size:22px;font-weight:600;color:var(--ink);display:block;margin-top:8px}
.field em{position:absolute;right:32px;top:56px;border:5px solid transparent;border-top-color:#222}
.form .go{flex:1;background:var(--orange);color:#fff;font-size:22px;font-weight:600;display:flex;align-items:center;justify-content:center}
.about{top:1276px;left:0;width:1200px;height:560px;background:var(--gray-bg)}
.ph{background:linear-gradient(135deg,#b9a18c,#e0d5c8)}
.about-text{left:613px;top:1366px;width:497px}
.about-text p{font-size:16px;line-height:31px;color:var(--ink);text-align:justify;margin-top:18px}
.btn{background:var(--orange);color:#fff;border-radius:28px;display:inline-flex;align-items:center;justify-content:center;gap:8px;font-weight:600}
.step{width:178px;height:178px;border-radius:50%;background:linear-gradient(135deg,#7b8ea6,#d9c8b6)}
.step b{position:absolute;left:-2px;top:-2px;width:55px;height:55px;border-radius:50%;background:var(--orange);border:6px solid #f7a36a;color:#fff;font-size:17px;font-weight:500;display:flex;align-items:center;justify-content:center}
.step-label{width:260px;text-align:center;font-size:20px;font-weight:600;color:var(--ink)}
.card{top:2750px;width:322px;height:385px;background:#fff;box-shadow:0 0 10px rgba(0,0,0,.12);text-align:center;padding-top:36px}
.card .ic{width:108px;height:108px;border-radius:50%;background:var(--orange);margin:0 auto;display:flex;align-items:center;justify-content:center}
.card h3{color:var(--green);font-size:17px;font-weight:700;margin-top:28px}
.card p{font-size:14px;line-height:28px;color:var(--ink);padding:12px 26px 0}
.card .btn{width:164px;height:41px;font-size:14px;margin-top:20px}
.footer{top:3211px;left:0;width:1200px;height:557px;background:linear-gradient(180deg,#444 0%,#2f2f2f 100%);color:#fff}
.fic{width:98px;height:98px;border-radius:50%;background:var(--green);border:5px solid #fff;display:flex;align-items:center;justify-content:center}
.finfo{width:300px;text-align:center;font-size:18px;line-height:29px}
.fnav{top:3609px;font-size:18px;color:#fff}
.fnav span{margin:0 12px}
.social{top:3714px;left:0;width:1200px;display:flex;justify-content:center;gap:7px}
.social i{width:30px;height:30px;border:2px solid #fff;border-radius:50%;display:block}
</style>
</head>
<body>

<div class="abs topbar">
  <div class="sep" style="left:90px"></div>
  <span style="left:116px">✉ hello@brightpathhome.example</span>
  <div class="sep" style="left:362px"></div>
  <span style="left:737px">EN ▾</span>
  <div class="sep" style="left:790px"></div>
  <span style="left:808px">● 118 Maple Grove Lane, Fairview, OH - 45000</span>
  <div class="sep" style="left:1110px"></div>
</div>

<div class="abs header">
  <div class="abs call">
    <div class="ring"><svg width="20" height="20" viewBox="0 0 24 24"><path d="M6.6 10.8a15 15 0 006.6 6.6l2.2-2.2c.3-.3.7-.4 1-.2 1.1.4 2.3.6 3.6.6.6 0 1 .4 1 1V20c0 .6-.4 1-1 1A17 17 0 013 4c0-.6.4-1 1-1h3.5c.6 0 1 .4 1 1 0 1.3.2 2.5.6 3.6.1.3 0 .7-.2 1z" fill="#f96f10"/></svg></div>
    <div><b>Call us:</b><small>+ 555-014-2277</small></div>
  </div>
  <div class="abs brand">Brightpath<small>HOME PARTNERS, LLC</small></div>
  <div class="abs search">Search<i><svg width="14" height="14" viewBox="0 0 24 24"><circle cx="10" cy="10" r="6" stroke="#fff" stroke-width="3" fill="none"/><path d="M15 15l5 5" stroke="#fff" stroke-width="3"/></svg></i></div>
</div>

<nav class="abs nav">
  <span>HOME</span><span>ABOUT US</span><span>OUR SERVICES</span><span>OUR PROCESS</span><span>OUR BLOG</span><span>TESTIMONIALS</span><span>CONTACT US</span>
</nav>

<div class="abs hero" role="img" aria-label="Caregiver gently supporting a smiling senior woman in a cosy living room"></div>
<div class="abs hero-name">Brightpath<small>HOME PARTNERS, LLC</small></div>
<svg class="abs" style="top:760px;left:0" width="1200" height="140" viewBox="0 0 1200 140">
  <path d="M0 132 Q600 40 1200 132 L1200 140 L0 140Z" fill="#fff"/>
  <path d="M110 118 Q600 50 1090 118 Q600 66 110 118Z" fill="#f96f10"/>
  <circle cx="600" cy="62" r="32" fill="#fff"/>
  <rect x="588" y="42" width="24" height="38" rx="12" fill="none" stroke="#333" stroke-width="2.5"/>
  <line x1="600" y1="48" x2="600" y2="56" stroke="#333" stroke-width="2.5"/>
</svg>

<h2 class="abs center" style="top:968px">FREE CONSULTATION</h2>
<p class="abs center lead" style="top:1034px">Sed ut perspiciatis unde omnis iste natus error sit voluptatem accusantium doloremque laudantium</p>

<div class="abs form">
  <div class="field"><small>Select your location</small><span>Choose a location</span><em></em></div>
  <div class="field"><small>Select your service</small><span>Choose a Service</span><em></em></div>
  <div class="go">Get care now</div>
</div>

<section class="abs about">
  <div class="abs ph" style="left:29px;top:116px;width:182px;height:118px" role="img" aria-label="Nurse checking an elderly woman's blood pressure"></div>
  <div class="abs ph" style="left:388px;top:80px;width:178px;height:118px" role="img" aria-label="Caregiver sitting with a senior woman"></div>
  <div class="abs ph" style="left:169px;top:176px;width:304px;height:210px" role="img" aria-label="Carer chatting with two smiling seniors"></div>
  <div class="abs ph" style="left:48px;top:343px;width:178px;height:118px" role="img" aria-label="Caregiver helping an older woman in an armchair"></div>
  <svg class="abs" style="left:376px;top:300px" width="176" height="176" viewBox="0 0 176 176">
    <circle cx="88" cy="88" r="84" fill="none" stroke="#333" stroke-dasharray="2 4"/>
    <circle cx="88" cy="88" r="62" fill="none" stroke="#555" stroke-dasharray="2 4"/>
    <circle cx="86" cy="82" r="40" fill="#fff"/>
    <circle cx="86" cy="82" r="14" fill="#2f8a0c"/>
  </svg>
</section>
<div class="abs about-text">
  <div class="kicker">ABOUT US</div>
  <h2 style="margin-top:14px">WHO WE ARE</h2>
  <p>Sed ut perspiciatis unde omnis iste natus error sit voluptatem accusantium doloremque laudantium, totam rem aperiam, eaque ipsa quae ab illo inventore veritatis et quasi architecto beatae vitae dicta sunt explicabo. Nemo enim ipsam voluptatem quia voluptas sit aspernatur aut odit aut fugit, sed quia consequuntur magni sequi nesciunt.</p>
  <div class="btn" style="width:206px;height:56px;font-size:18px;margin-top:24px">Read More <svg width="16" height="16" viewBox="0 0 16 16"><circle cx="8" cy="8" r="8" fill="#fff"/><path d="M5 8h6M8 5l3 3-3 3" stroke="#f96f10" stroke-width="2" fill="none"/></svg></div>
</div>
<svg class="abs" style="top:1800px;left:0" width="1200" height="110" viewBox="0 0 1200 110">
  <path d="M0 36 L600 20 Q900 14 1200 30 L1200 110 L0 110Z" fill="#fff"/>
  <path d="M0 108 Q200 40 630 20 Q200 60 0 78Z" fill="#f96f10"/>
</svg>

<div class="abs center kicker" style="top:1937px">OUR PROCESS</div>
<h2 class="abs center" style="top:1970px">HOW IT HELPS YOU STAY STRONG</h2>
<p class="abs center lead" style="top:2031px">Sed ut perspiciatis unde omnis iste natus error sit voluptatem accusantium doloremque laudantium, totam rem aperiam,<br>eaque ipsa quae ab illo inventore veritatis et quasi architecto beatae vitae dicta sunt explicabo.</p>
<svg class="abs" style="top:2120px;left:0" width="1200" height="200" viewBox="0 0 1200 200">
  <path d="M0 170 Q100 110 200 100 Q350 70 470 92 Q600 120 730 118 Q870 130 1010 100 Q1110 80 1190 30" fill="none" stroke="#999" stroke-dasharray="6 6"/>
  <circle cx="2" cy="166" r="4" fill="none" stroke="#333"/>
  <path d="M1170 30h8l4-8 5 14 4-6h8" fill="none" stroke="#333" stroke-width="1.5"/>
</svg>
<div class="abs step" style="left:108px;top:2132px" role="img" aria-label="Nurse chatting with a senior man"><b>01</b></div>
<div class="abs step" style="left:378px;top:2132px" role="img" aria-label="Nurse taking a senior's blood pressure"><b>02</b></div>
<div class="abs step" style="left:645px;top:2132px" role="img" aria-label="Carer consulting with an older woman"><b>03</b></div>
<div class="abs step" style="left:918px;top:2132px" role="img" aria-label="Caregiver serving a meal to a senior man"><b>04</b></div>
<div class="abs step-label" style="left:67px;top:2346px">APPLICATION</div>
<div class="abs step-label" style="left:337px;top:2346px">CHECK-UPS</div>
<div class="abs step-label" style="left:604px;top:2346px">CONSULTATION</div>
<div class="abs step-label" style="left:877px;top:2346px">SCHEMING</div>
<svg class="abs" style="top:2400px;left:640px" width="560" height="90" viewBox="0 0 560 90">
  <path d="M10 86 Q350 70 560 0 L560 32 Q350 80 10 86Z" fill="#f96f10"/>
</svg>

<div class="abs center kicker" style="top:2563px">OUR SERVICES</div>
<h2 class="abs center" style="top:2604px">MANAGED HEATHCARE SERVICES</h2>
<p class="abs center lead" style="top:2660px">Sed ut perspiciatis unde omnis iste natus error sit voluptatem accusantium doloremque laudantium, totam rem aperiam,<br>eaque ipsa quae ab illo inventore veritatis et quasi architecto beatae vitae dicta sunt explicabo.</p>

<div class="abs card" style="left:89px">
  <div class="ic"><svg width="54" height="54" viewBox="0 0 24 24" fill="none" stroke="#fff" stroke-width="1.3"><path d="M12 18s-5-3-5-6.5A2.5 2.5 0 0112 10a2.5 2.5 0 015 1.5C17 15 12 18 12 18z"/><path d="M2 14l3 3h5M22 10l-3-3h-5"/></svg></div>
  <h3>DAILY HOME CARE</h3>
  <p>Sed ut perspiciatis unde omnis iste natus error sit voluptatem accusantium doloremque explicabo.</p>
  <div class="btn">More Details »</div>
</div>
<div class="abs card" style="left:439px">
  <div class="ic"><svg width="54" height="54" viewBox="0 0 24 24" fill="none" stroke="#fff" stroke-width="1.3"><rect x="6" y="7" width="10" height="13" rx="2"/><rect x="7" y="3" width="8" height="4"/><path d="M11 11v5M8.5 13.5h5"/><circle cx="18" cy="17" r="3"/></svg></div>
  <h3>SPECIALIZED CARE</h3>
  <p>Sed ut perspiciatis unde omnis iste natus error sit voluptatem accusantium doloremque explicabo.</p>
  <div class="btn">More Details »</div>
</div>
<div class="abs card" style="left:787px">
  <div class="ic"><svg width="54" height="54" viewBox="0 0 24 24" fill="none" stroke="#fff" stroke-width="1.3"><path d="M12 11s-3-2-3-4a1.5 1.5 0 013-.5 1.5 1.5 0 013 .5c0 2-3 4-3 4z"/><path d="M3 15h5l4 2h6l3-3M3 19h14"/></svg></div>
  <h3>HOURLY HOME CARE</h3>
  <p>Sed ut perspiciatis unde omnis iste natus error sit voluptatem accusantium doloremque explicabo.</p>
  <div class="btn">More Details »</div>
</div>

<footer class="abs footer" role="img" aria-label="Dimmed photo of a caregiver with an elderly person"></footer>
<svg class="abs" style="top:3205px;left:0" width="1200" height="110" viewBox="0 0 1200 110">
  <path d="M0 6 Q600 110 1200 6 L1200 0 L0 0Z" fill="#fff"/>
  <path d="M110 20 Q600 90 1090 20 Q600 74 110 20Z" fill="#f96f10"/>
  <circle cx="600" cy="80" r="30" fill="#fff"/>
  <rect x="588" y="62" width="24" height="36" rx="12" fill="none" stroke="#333" stroke-width="2.5"/>
  <line x1="600" y1="68" x2="600" y2="76" stroke="#333" stroke-width="2.5"/>
</svg>
<div class="abs fic" style="left:248px;top:3425px"><svg width="44" height="44" viewBox="0 0 24 24" fill="none" stroke="#fff" stroke-width="1.3"><path d="M12 21s-6-6-6-11a6 6 0 0112 0c0 5-6 11-6 11z"/><circle cx="12" cy="10" r="2.2"/></svg></div>
<div class="abs fic" style="left:564px;top:3425px"><svg width="44" height="44" viewBox="0 0 24 24" fill="none" stroke="#fff" stroke-width="1.3"><rect x="3" y="6" width="18" height="12"/><path d="M3 6l9 7 9-7M3 18l7-6M21 18l-7-6"/></svg></div>
<div class="abs fic" style="left:884px;top:3425px"><svg width="44" height="44" viewBox="0 0 24 24" fill="none" stroke="#fff" stroke-width="1.3"><path d="M6.6 10.8a15 15 0 006.6 6.6l2.2-2.2c.3-.3.7-.4 1-.2 1.1.4 2.3.6 3.6.6.6 0 1 .4 1 1V20c0 .6-.4 1-1 1A17 17 0 013 4c0-.6.4-1 1-1h3.5c.6 0 1 .4 1 1 0 1.3.2 2.5.6 3.6.1.3 0 .7-.2 1z"/></svg></div>
<div class="abs finfo" style="left:147px;top:3524px;color:#fff">42 Willow Bend Drive,<br>Ashford, CT - 06000</div>
<div class="abs finfo" style="left:463px;top:3524px;color:#fff">Email:<br>hello@brightpathhome.example</div>
<div class="abs finfo" style="left:783px;top:3524px;color:#fff">Phone:<br>555 014 2277</div>
<div class="abs center fnav">HOME<span>|</span>ABOUT US<span>|</span>OUR SERVICES<span>|</span>OUR PROCESS<span>|</span>OUR BLOG<span>|</span>TESTIMONIALS<span>|</span>CONTACT US<span>|</span></div>
<div class="abs center" style="top:3662px;color:#fff;font-size:16px">© Brightpath Home Partners 2019. All rights reserved</div>
<div class="abs social"><i></i><i></i><i></i><i></i></div>

</body>
</html>
```